Create a 3.5" x 8.5" door hanger for a produce delivery company called Uncle Fennel's.

Door hanger should fit the template specifications attached.

Door hanger should include some form of the logo attached.

Door hanger should include the information: "Fresh, local produce, meats, dairy, cheese, and baked goods. Delivered to your door at grocery store prices!"

Door hanger should include the following coupon: "$15.00 OFF! Enter coupon code “doorhanger” during sign up and we’ll waive the enrollment fee and take $5.00 of your first order!"

Door hanger should have the website printed noticeably: UncleFennels.com

Door hanger should include photos of seasonal produce items to the southern US. Some examples include: apples, pumpkins, bell peppers, squashes, eggplant, tomatoes, green beans, carrots, broccoli, greens, sweet potatoes, lettuces, cauliflower, cabbage, radishes.

Industry/Entity Type

Grocery Store

Requirements
Nice to have
• A back side with some or all of the following "About us" information:
• Uncle Fennel's is a farm to fork delivery service, working to bring the entire NC food landscape to your front door! Since 2008 we have been expanding our network of local growers and food artisans, and are happy to be able to offer over 200 food products a week, and we are still growing! Our goal is to greatly improve access to local foods in our community through transparency, communication, affordability, and the convenience of our delivery infrastructure.
• Here are just a few reasons we think you will love working with Uncle Fennel's:
• Wide variety of NC products!
• You will not find a greater variety of NC produce anywhere else, outside of a farmers market.
• Superior freshness, quality, and flavor!
• By working with local growers, products can be fully ripened on the vine, picked and delivered to your door within 48 hours of harvest.
• Affordable!
• We understand that affordability is an important concern for every family. On average our prices are equivalent to grocery store prices when comparing like items (organic to organic, etc.).
• Support your community!
• By purchasing from local farms and food artisans, you are supporting your neighbors and helping to further develop our local food infrastructure.
• Educational!
• Purchasing seasonal products from local farms is a fantastic opportunity to get back to nature and reconnect with what food really is.
• Convenient and easy!
• Not to mention, we deliver to your front door! Easy!

```html
<!DOCTYPE html>
<html lang="en">
<head>
<meta charset="utf-8">
<title>Uncle Fennel's Door Hangers</title>
<link rel="stylesheet" href="https://fonts.googleapis.com/css2?family=Kaushan+Script&family=Lobster&family=Courgette&family=Patrick+Hand&family=Archivo+Narrow:wght@700&family=Arimo:wght@400;700&display=swap">
<style>
:root{
  --paper:#ffffff;
  --ink:#111111;
  --orange:#f07a12;
  --cauli:#ece6d6;
  --lettuce:#6fae2e;
  --pumpkin:#f39a2a;
  --band-black:#000000;
  --red:#d8141a;
  --green-dark:#2b6a3f;
  --green-text:#1f6b35;
  --green-light:#bff5a0;
  --cream:#eef0ea;
}
*{margin:0;padding:0;box-sizing:border-box}
html,body{width:1097px;height:1200px;overflow:hidden;background:var(--paper)}
.canvas{position:relative;width:1097px;height:1200px}
.hanger{position:absolute;top:0;height:1200px;overflow:hidden}
.hanger--bold{left:0;width:526px;background:var(--paper)}
.hanger--fresh{left:572px;width:525px;background:var(--cream);box-shadow:-3px 0 8px rgba(0,0,0,.15)}
.hole{position:absolute;border-radius:50%;background:var(--paper)}
.abs{position:absolute}

/* bold hanger */
.strip{position:absolute;top:0;height:666px}
.strip--cauliflower{left:0;width:174px;background:radial-gradient(circle at 40% 40%,#fbf8ef,var(--cauli) 60%,#cfc6ad)}
.strip--lettuce{left:180px;width:171px;background:linear-gradient(160deg,#9fd35a,var(--lettuce) 50%,#3f8a1c)}
.strip--pumpkin{left:357px;width:169px;background:linear-gradient(170deg,#f6b24e,var(--pumpkin) 50%,#e06e0c)}
.bold-headline{left:0;width:526px;top:300px;text-align:center;font-family:"Kaushan Script",cursive;font-weight:400;font-size:45px;line-height:54px;color:var(--ink);text-shadow:0 0 3px var(--orange),0 0 3px var(--orange),0 0 3px var(--orange),2px 2px 0 var(--orange),-2px -2px 0 var(--orange),2px -2px 0 var(--orange),-2px 2px 0 var(--orange)}
.bold-sub{left:0;width:526px;top:505px;text-align:center;font-family:"Archivo Narrow",sans-serif;font-weight:700;font-size:32px;line-height:38px;color:var(--ink);text-shadow:2px 2px 0 #fff,-2px -2px 0 #fff,2px -2px 0 #fff,-2px 2px 0 #fff}
.band-black{left:0;top:666px;width:526px;height:402px;background:var(--band-black)}
.burst{position:absolute}
.burst-text{position:absolute;text-align:center;font-family:"Lobster",cursive;line-height:1}
.coupon{position:absolute;text-align:center;font-family:"Arimo",sans-serif;font-size:19px;line-height:33px}
.coupon--light{left:0;width:526px;top:946px;color:#fff}
.footer-bold{left:0;top:1068px;width:526px;height:132px;background:var(--paper)}
.brand{position:absolute;display:flex;flex-direction:column;align-items:center;gap:3px;width:120px;font-family:"Arimo",sans-serif;font-weight:700;font-size:11px}
.brand-dot{width:34px;height:34px;border-radius:50%;border:2px solid currentColor;flex:none}
.site{position:absolute;white-space:nowrap}
.site--bold{left:146px;top:1104px;font-family:"Arimo",sans-serif;font-weight:700;font-size:31px;color:var(--ink)}

/* fresh hanger */
.mosaic{left:0;top:0;width:525px;height:288px;background:linear-gradient(180deg,rgba(238,240,234,0) 55%,var(--cream)),conic-gradient(from 30deg,#c9352a,#7fb04a,#e9a93c,#8a5a3a,#d64a3a,#6c9a3c,#c9352a)}
.produce{position:absolute;border-radius:50%}
.fresh-headline{left:100px;width:255px;top:330px;text-align:center;font-family:"Courgette",cursive;font-weight:400;font-size:32px;line-height:41px;color:var(--red)}
.delivery-oval{left:30px;top:600px}
.fresh-sub{left:30px;width:420px;top:612px;text-align:center;font-family:"Patrick Hand",cursive;font-size:37px;line-height:44px;color:var(--green-text)}
.tomatoes{left:0;top:716px;width:272px;height:228px;border-radius:0 45% 40% 0;background:radial-gradient(circle at 55% 45%,#ff5a3a,#d8261a 45%,rgba(216,38,26,0) 72%),radial-gradient(circle at 12% 55%,#e8c3c8,rgba(232,195,200,0) 45%)}
.coupon--dark{left:0;width:525px;top:966px;color:var(--ink);font-weight:700;line-height:30px}
.coupon--dark .code{color:#1f8a2a}
.coupon--dark .off{color:#c21a10}
.footer-fresh{left:0;top:1072px;width:525px;height:128px;background:var(--green-dark)}
.site--fresh{left:140px;width:375px;text-align:center;top:1110px;font-family:"Courgette",cursive;font-size:30px;color:var(--green-light)}
</style>
</head>
<body>
<main class="canvas">

  <section class="hanger hanger--bold">
    <div class="strip strip--cauliflower" role="img" aria-label="Close-up photo of cauliflower florets"></div>
    <div class="strip strip--lettuce" role="img" aria-label="Close-up photo of green lettuce leaves"></div>
    <div class="strip strip--pumpkin" role="img" aria-label="Close-up photo of cut pumpkin with seeds"></div>
    <div class="hole" style="left:176px;top:32px;width:176px;height:176px"></div>

    <h1 class="abs bold-headline">Fresh, local produce,<br>meats, dairy, cheese,<br>and baked goods.</h1>
    <p class="abs bold-sub">Delivered to your door<br>at grocery store prices!</p>

    <div class="abs band-black"></div>
    <svg class="burst" style="left:138px;top:678px" width="228" height="228" viewBox="-100 -100 200 200" aria-hidden="true">
      <polygon fill="#ffffff" points="100,0 85,13.4 95.1,30.9 76.6,39 80.9,58.8 60.8,60.8 58.8,80.9 39,76.6 30.9,95.1 13.4,85 0,100 -13.4,85 -30.9,95.1 -39,76.6 -58.8,80.9 -60.8,60.8 -80.9,58.8 -76.6,39 -95.1,30.9 -85,13.4 -100,0 -85,-13.4 -95.1,-30.9 -76.6,-39 -80.9,-58.8 -60.8,-60.8 -58.8,-80.9 -39,-76.6 -30.9,-95.1 -13.4,-85 0,-100 13.4,-85 30.9,-95.1 39,-76.6 58.8,-80.9 60.8,-60.8 80.9,-58.8 76.6,-39 95.1,-30.9 85,-13.4"/>
    </svg>
    <div class="burst-text" style="left:138px;width:228px;top:745px;color:var(--ink);font-size:44px">$15.00</div>
    <div class="burst-text" style="left:138px;width:228px;top:795px;color:var(--ink);font-size:58px">OFF!</div>

    <p class="coupon coupon--light">Enter coupon code “doorhanger” during<br>sign up and we’ll waive the enrollment fee<br>and take $5.00 of your first order!</p>

    <div class="abs footer-bold"></div>
    <div class="brand" style="left:12px;top:1100px;color:var(--ink)"><span class="brand-dot"></span><span>Uncle Fennel's</span></div>
    <div class="site site--bold">www.unclefennels.com</div>
  </section>

  <section class="hanger hanger--fresh">
    <div class="abs mosaic" role="img" aria-label="Grid of photos of fruits, vegetables, nuts and baked goods"></div>
    <div class="hole" style="left:154px;top:66px;width:180px;height:180px"></div>

    <div class="produce" style="left:38px;top:284px;width:110px;height:70px;background:radial-gradient(#8ec25a,#4c8a2a)" role="img" aria-label="Photo of lettuce leaf"></div>
    <div class="produce" style="left:48px;top:378px;width:72px;height:84px;background:radial-gradient(#e8382a,#a5140c)" role="img" aria-label="Photo of red bell peppers"></div>
    <div class="produce" style="left:44px;top:498px;width:104px;height:96px;background:radial-gradient(circle at 40% 35%,#d8ec7a,#8fbb2c)" role="img" aria-label="Photo of a green apple"></div>
    <div class="produce" style="left:350px;top:286px;width:130px;height:94px;background:radial-gradient(#7a4a7e,#3d1f45)" role="img" aria-label="Photo of eggplants"></div>
    <div class="produce" style="left:372px;top:404px;width:100px;height:96px;background:radial-gradient(#6aa03a,#2f6418)" role="img" aria-label="Photo of broccoli"></div>
    <div class="produce" style="left:368px;top:522px;width:110px;height:86px;background:radial-gradient(#b8685a,#6e3228)" role="img" aria-label="Photo of red potatoes"></div>

    <h2 class="abs fresh-headline">Fresh,<br>local produce,<br>meats, dairy,<br>cheese, and<br>baked goods.</h2>

    <svg class="abs delivery-oval" width="420" height="112" viewBox="0 0 420 112" aria-hidden="true">
      <ellipse cx="210" cy="56" rx="206" ry="52" fill="rgba(255,255,255,.55)" stroke="#333" stroke-width="1.5" stroke-dasharray="2 4"/>
    </svg>
    <p class="abs fresh-sub">Delivered to your door<br>at grocery store prices!</p>

    <div class="abs tomatoes" role="img" aria-label="Photo of vine tomatoes, garlic and green beans"></div>

    <svg class="burst" style="left:268px;top:718px" width="220" height="220" viewBox="-100 -100 200 200" aria-hidden="true">
      <defs><radialGradient id="greenBurst" cx="50%" cy="40%" r="60%"><stop offset="0" stop-color="#7fb04a"/><stop offset="1" stop-color="#2c6a2a"/></radialGradient></defs>
      <polygon fill="url(#greenBurst)" stroke="#fff" stroke-width="2" points="100,0 85,13.4 95.1,30.9 76.6,39 80.9,58.8 60.8,60.8 58.8,80.9 39,76.6 30.9,95.1 13.4,85 0,100 -13.4,85 -30.9,95.1 -39,76.6 -58.8,80.9 -60.8,60.8 -80.9,58.8 -76.6,39 -95.1,30.9 -85,13.4 -100,0 -85,-13.4 -95.1,-30.9 -76.6,-39 -80.9,-58.8 -60.8,-60.8 -58.8,-80.9 -39,-76.6 -30.9,-95.1 -13.4,-85 0,-100 13.4,-85 30.9,-95.1 39,-76.6 58.8,-80.9 60.8,-60.8 80.9,-58.8 76.6,-39 95.1,-30.9 85,-13.4"/>
    </svg>
    <div class="burst-text" style="left:268px;width:220px;top:776px;color:#fff;font-size:46px">$15.00</div>
    <div class="burst-text" style="left:268px;width:220px;top:826px;color:#fff;font-size:58px">OFF!</div>

    <p class="coupon coupon--dark">Enter coupon code “<span class="code">doorhanger</span>” during<br>sign up and we’ll waive the enrollment fee<br>and <span class="off">take $5.00</span> of your first order!</p>

    <div class="abs footer-fresh"></div>
    <div class="brand" style="left:20px;top:1104px;color:#fff"><span class="brand-dot"></span><span>Uncle Fennel's</span></div>
    <div class="site site--fresh">www.unclefennels.com</div>
  </section>

</main>
</body>
</html>
```